TKN Music Studios

I need a website for two locations, description of services, possible merchandise page, PDFs of faculty, bios, live performance of both faculty and students, testimonial page, pre-college prep page for musical theatre, links to our social media, link to our registration page, link to affiliate programming resources

```html
<!DOCTYPE html>
<html lang="en">
<head>
<meta charset="utf-8">
<title>TKN Music Studios</title>
<link rel="stylesheet" href="https://fonts.googleapis.com/css2?family=Pinyon+Script&family=Lato:wght@400;700;900&display=swap">
<style>
:root{
  --bg:#2b2c3a;
  --bg-dark:#22232e;
  --bg-panel:#1d1e27;
  --pink:#ff0d6e;
  --text:#e6e6ea;
  --muted:#b9bac4;
  --line:#9a9aa6;
}
*{box-sizing:border-box;margin:0;padding:0}
html,body{width:1200px;height:4518px;overflow:hidden;background:var(--bg);color:var(--text);font-family:"Lato",sans-serif}
.page{position:relative;width:1200px;height:4518px}
section,header,footer{position:absolute;left:0;width:1200px}
.abs{position:absolute}
.script{font-family:"Pinyon Script",cursive;font-weight:400;letter-spacing:.5px}
.btn{position:absolute;display:flex;align-items:center;justify-content:center;border:2px solid var(--pink);color:#fff;font-weight:900;font-size:14px;letter-spacing:.5px;text-transform:uppercase}
.photo{position:absolute}
.heading{position:absolute;left:0;display:flex;align-items:center;font-size:36px;color:#fff;white-space:nowrap}
.heading::before{content:"";display:block;width:70px;height:2px;background:var(--pink);margin-right:18px}
.heading em{font-style:normal;color:var(--pink);margin-left:12px}
.body-text{position:absolute;font-size:14px;line-height:27.5px;color:var(--text)}
.arrow{position:absolute;width:39px;height:39px;border:2px solid var(--pink);display:flex;align-items:center;justify-content:center}
.arrow svg{width:12px;height:12px}

/* header */
.site-header{top:0;height:147px;background:var(--bg)}
.logo{left:74px;top:30px;font-size:38px;line-height:42px;color:#fff}
.nav{left:0;width:1200px;display:flex;justify-content:space-between;padding:0 82px;align-items:center}
.nav span{font-size:11.5px;font-weight:900;text-transform:uppercase;color:#fff;white-space:nowrap}
.main-nav{top:147px;height:62px;background:var(--pink)}

/* hero */
.hero{top:209px;height:617px;background:radial-gradient(ellipse at 45% 40%,#4a4350 0%,#2a2530 40%,#15141c 100%)}
.hero-title{left:0;width:1200px;top:222px;text-align:center;font-size:80px;line-height:78px;color:#fff;white-space:nowrap}

/* about */
.about{top:826px;height:449px;background:var(--bg)}

/* services */
.services{top:1275px;height:493px;background:linear-gradient(100deg,#23222a 0%,#35302e 45%,#2a2020 70%,#3a2a24 100%)}
.service-card{position:absolute;top:133px;width:330px;height:299px;border:2px solid #bfbfc6;text-align:center;background:rgba(20,20,26,.35)}
.service-card svg{margin-top:32px;width:92px;height:82px}
.service-card h3{margin-top:22px;font-weight:400;font-size:24px;color:var(--pink)}
.service-card p{margin:18px auto 0;width:270px;font-size:14px;line-height:28px;color:#fff}

/* live */
.live{top:1768px;height:849px;background:var(--bg)}
.perf{position:absolute;width:330px;height:306px}
.perf.active{border:5px solid var(--pink)}

/* bios */
.bios{top:2617px;height:461px;background:var(--bg-dark)}
.bio{position:absolute;top:139px;width:243px}
.bio .portrait{position:relative;height:212px}
.bio .name{position:absolute;left:10px;right:10px;bottom:0;height:46px;background:rgba(40,40,50,.75);display:flex;align-items:center;justify-content:center;font-size:22px;color:#ddd;white-space:nowrap}
.bio p{text-align:center;font-size:14px;margin-top:8px;color:#fff}
.bio .social{display:flex;justify-content:center;gap:18px;margin-top:16px}
.bio .social i{display:block;width:13px;height:13px;border-radius:50%;background:var(--pink)}

/* pre-college */
.precollege{top:3078px;height:435px;background:var(--bg)}

/* testimonials */
.testimonials{top:3513px;height:384px;background:var(--bg-dark)}
.quote{position:absolute;top:125px;width:330px}
.quote .mark{font-family:Georgia,serif;font-size:90px;line-height:60px;color:#55565f;height:40px}
.quote p{font-size:14px;line-height:28px;color:#fff;margin-top:-10px}
.quote .who{margin-top:17px;color:var(--pink);font-size:14px;font-weight:700}

/* locations */
.locations{top:3897px;height:453px;background:var(--bg)}
.map{position:absolute;top:125px;width:277px;height:261px;border:4px solid #c9c9d0;background:linear-gradient(135deg,#e9eaec,#d5d8dc)}
.loc-info{position:absolute;top:158px;width:283px;height:195px;background:var(--bg-panel);padding:26px 18px}
.loc-info h4{color:var(--pink);font-weight:400;font-size:18px;margin-bottom:10px}
.loc-row{display:flex;gap:14px;font-size:14px;line-height:25px;color:#fff;margin-bottom:4px}
.loc-row svg{flex:none;width:14px;height:14px;margin-top:6px}

/* footer */
.site-footer{top:4350px;height:168px;background:var(--bg-dark)}
.footer-nav{top:38px}
.copy{top:75px;left:0;width:1200px;text-align:center;font-size:12px;color:var(--muted)}
.footer-social{top:101px;left:0;width:1200px;display:flex;justify-content:center;gap:10px}
.footer-social i{display:block;width:38px;height:38px;border:2px solid var(--pink);border-radius:50%}
</style>
</head>
<body>
<div class="page">

<header class="site-header">
  <div class="abs logo script">TKN Music<br>Studios</div>
  <a class="btn" style="left:847px;top:54px;width:156px;height:42px;font-size:13px">Download PDF</a>
  <a class="btn" style="left:1021px;top:54px;width:105px;height:42px;font-size:13px">Register</a>
</header>

<nav class="abs nav main-nav">
  <span>About Us</span><span>Services</span><span>Bio's</span><span>Live Performance</span><span>Testimonials</span><span>Pre-College Prep</span><span>Affiliate Program</span><span>Shop</span><span>Contact Us</span>
</nav>

<section class="hero" role="img" aria-label="Singer in a gown performing with a conducted orchestra on stage">
  <svg class="abs" style="left:60px;top:290px" width="20" height="36" viewBox="0 0 20 36"><path d="M18 2 2 18l16 16" fill="none" stroke="#ddd" stroke-width="2"/></svg>
  <svg class="abs" style="left:1120px;top:290px" width="20" height="36" viewBox="0 0 20 36"><path d="M2 2l16 16L2 34" fill="none" stroke="#ddd" stroke-width="2"/></svg>
  <h1 class="abs hero-title script">Welcome to<br>TKN Music Studios</h1>
</section>

<section class="about">
  <h2 class="heading script" style="top:60px">About <em>TKN Music Studios</em></h2>
  <p class="body-text" style="left:74px;top:128px;width:510px">Lorem ipsum dolor sit amet, consectetur adipiscing elit. Maecenas sit amet velit egestas, egestas diam eu, aliquam odio. Nullam tempus tortor a sapien lacinia, non pellentesque elit pulvinar. Proin aliquam aliquam accumsan. Nullam euismod ullamcorper mi non pulvinar. Sed sollicitudin ex non mi ultricies, in fringilla magna cursus. Quisque tincidunt convallis nulla, eu dignissim felis vulputate et.</p>
  <a class="btn" style="left:74px;top:325px;width:179px;height:47px">Read More</a>
  <div class="photo" style="left:616px;top:74px;width:247px;height:303px;background:linear-gradient(160deg,#8a3a30,#4b2a25 60%,#2a2224)" role="img" aria-label="Two studio founders standing by a piano"></div>
  <div class="photo" style="left:877px;top:74px;width:249px;height:303px;background:linear-gradient(160deg,#5a5450,#2c2826 60%,#1a1818)" role="img" aria-label="Songwriter taking notes in a recording studio"></div>
</section>

<section class="services" role="img" aria-label="Dim stage and theatre backdrop">
  <h2 class="heading script" style="top:60px">Our <em>Services</em></h2>
  <div class="arrow" style="left:1033px;top:63px"><svg viewBox="0 0 12 12"><path d="M8 1 3 6l5 5" fill="none" stroke="#ff0d6e" stroke-width="2"/></svg></div>
  <div class="arrow" style="left:1087px;top:63px"><svg viewBox="0 0 12 12"><path d="M4 1l5 5-5 5" fill="none" stroke="#ff0d6e" stroke-width="2"/></svg></div>

  <div class="service-card" style="left:74px">
    <svg viewBox="0 0 92 82" fill="none" stroke="#fff" stroke-width="3"><rect x="6" y="6" width="80" height="58" rx="3"/><path d="M46 6v58M16 20h20M16 30h20M56 20h20M56 30h20"/><circle cx="46" cy="58" r="20" fill="#2a2630"/><path d="M41 48v20l15-10z" fill="#fff" stroke="none"/></svg>
    <h3>Music Lessons</h3>
    <p>Neque porro quisquam est qui dolorem ipsum quia dolor sit amet, consectetur, adipisci velit torquent.</p>
  </div>
  <div class="service-card" style="left:435px">
    <svg viewBox="0 0 92 82" fill="none" stroke="#fff" stroke-width="3"><rect x="10" y="30" width="34" height="44" rx="3"/><path d="M22 62V44l14-4v18"/><circle cx="19" cy="62" r="4"/><circle cx="33" cy="58" r="4"/><path d="M50 56l34-34M78 14l8 8"/><circle cx="54" cy="52" r="9"/></svg>
    <h3>Song Writing</h3>
    <p>Neque porro quisquam est qui dolorem ipsum quia dolor sit amet, consectetur, adipisci velit torquent.</p>
  </div>
  <div class="service-card" style="left:796px">
    <svg viewBox="0 0 92 82" fill="none" stroke="#fff" stroke-width="3"><rect x="18" y="10" width="48" height="64" rx="3"/><path d="M32 10V4h20v6M28 30h28M28 42h28M28 54h16"/><circle cx="70" cy="56" r="14" fill="#2a2630"/><path d="M63 56l5 5 9-10"/></svg>
    <h3>Audition Prep</h3>
    <p>Neque porro quisquam est qui dolorem ipsum quia dolor sit amet, consectetur, adipisci velit torquent.</p>
  </div>
</section>

<section class="live">
  <h2 class="heading script" style="top:54px">Live <em>Performance</em></h2>
  <a class="btn" style="left:947px;top:56px;width:179px;height:46px">View All</a>
  <div class="perf active" style="left:74px;top:133px;background:linear-gradient(150deg,#c84a7a,#7a2a48 55%,#2a1a24)" role="img" aria-label="Student singing on a pink-lit stage"></div>
  <div class="perf" style="left:435px;top:133px;background:linear-gradient(160deg,#d8d4d0,#8a8480 55%,#3a3634)" role="img" aria-label="Singer fronting a live band"></div>
  <div class="perf" style="left:796px;top:133px;background:linear-gradient(160deg,#3a3a3e,#1a1a1e 50%,#111)" role="img" aria-label="Vocalist singing into a microphone"></div>
  <div class="perf" style="left:74px;top:474px;background:linear-gradient(150deg,#3a2a80,#6a2a8a 55%,#1a1430)" role="img" aria-label="Performers seated on a purple-lit stage"></div>
  <div class="perf" style="left:435px;top:474px;background:linear-gradient(160deg,#7a1a20,#3a1a1c 55%,#141014)" role="img" aria-label="Cast in costume performing a musical number"></div>
  <div class="perf" style="left:796px;top:474px;background:linear-gradient(160deg,#2a2228,#161218 60%,#0e0c10)" role="img" aria-label="Male singer performing on a dark stage"></div>
</section>

<section class="bios">
  <h2 class="heading script" style="top:60px">Our <em>Bio's</em></h2>
  <div class="arrow" style="left:1033px;top:64px"><svg viewBox="0 0 12 12"><path d="M8 1 3 6l5 5" fill="none" stroke="#ff0d6e" stroke-width="2"/></svg></div>
  <div class="arrow" style="left:1087px;top:64px"><svg viewBox="0 0 12 12"><path d="M4 1l5 5-5 5" fill="none" stroke="#ff0d6e" stroke-width="2"/></svg></div>

  <div class="bio" style="left:74px">
    <div class="portrait" style="background:linear-gradient(160deg,#c9a070,#8a6a4a 60%,#4a3a30)" role="img" aria-label="Portrait of faculty member Marisol Vega"><div class="name script">Marisol Vega</div></div>
    <p>Lorem ipsum dolor</p><div class="social"><i></i><i></i><i></i><i></i></div>
  </div>
  <div class="bio" style="left:344px">
    <div class="portrait" style="background:linear-gradient(160deg,#6a5a4a,#3a3028 60%,#221c18)" role="img" aria-label="Portrait of faculty member Daniel Hartwell"><div class="name script">Daniel Hartwell</div></div>
    <p>Lorem ipsum dolor</p><div class="social"><i></i><i></i><i></i><i></i></div>
  </div>
  <div class="bio" style="left:614px">
    <div class="portrait" style="background:linear-gradient(160deg,#5a4038,#3a2420 60%,#1e1414)" role="img" aria-label="Portrait of faculty member Inés Castillo"><div class="name script">Inés Castillo</div></div>
    <p>Lorem ipsum dolor</p><div class="social"><i></i><i></i><i></i><i></i></div>
  </div>
  <div class="bio" style="left:884px">
    <div class="portrait" style="background:linear-gradient(160deg,#7a8a6a,#8a7058 60%,#4a3a30)" role="img" aria-label="Portrait of faculty member Claire Donovan"><div class="name script">Claire Donovan</div></div>
    <p>Lorem ipsum dolor</p><div class="social"><i></i><i></i><i></i><i></i></div>
  </div>
</section>

<section class="precollege">
  <h2 class="heading script" style="top:60px">Pre-College <em>Prepration</em></h2>
  <p class="body-text" style="left:74px;top:112px;width:510px">Lorem ipsum dolor sit amet, consectetur adipiscing elit. Maecenas sit amet velit egestas, egestas diam eu, aliquam odio. Nullam tempus tortor a sapien lacinia, non pellentesque elit pulvinar. Proin aliquam aliquam accumsan. Nullam euismod ullamcorper mi non pulvinar. Sed sollicitudin ex non mi ultricies, in fringilla magna cursus. Quisque tincidunt convallis nulla, eu dignissim felis vulputate et.</p>
  <a class="btn" style="left:74px;top:314px;width:179px;height:46px">Read More</a>
  <div class="photo" style="left:616px;top:62px;width:247px;height:303px;background:linear-gradient(160deg,#6a4a30,#3a2818 60%,#1e140c)" role="img" aria-label="Student playing a ukulele in sepia tones"></div>
  <div class="photo" style="left:877px;top:62px;width:249px;height:303px;background:linear-gradient(180deg,#6a3a6a,#2a1a4a 50%,#120e20)" role="img" aria-label="Ensemble of students in black on stage"></div>
</section>

<section class="testimonials">
  <h2 class="heading script" style="top:62px">Our <em>Testimonial</em></h2>
  <div class="arrow" style="left:1033px;top:65px"><svg viewBox="0 0 12 12"><path d="M8 1 3 6l5 5" fill="none" stroke="#ff0d6e" stroke-width="2"/></svg></div>
  <div class="arrow" style="left:1087px;top:65px"><svg viewBox="0 0 12 12"><path d="M4 1l5 5-5 5" fill="none" stroke="#ff0d6e" stroke-width="2"/></svg></div>
  <div class="quote" style="left:74px"><div class="mark">“</div><p>" Lorem ipsum dolor sit amet, consectetur adipiscing elit. Maecenas sit amet velit egestas, egestas diam eu, aliquam odio ullam tempus tortor a sapien lacinia, non pellentesque elit pulvinar est qui dolorem .."</p><div class="who">- NOAH R.</div></div>
  <div class="quote" style="left:435px"><div class="mark">“</div><p>" Lorem ipsum dolor sit amet, consectetur adipiscing elit. Maecenas sit amet velit egestas, egestas diam eu, aliquam odio ullam tempus tortor a sapien lacinia, non pellentesque elit pulvinar est qui dolorem .."</p><div class="who">- NOAH R.</div></div>
  <div class="quote" style="left:795px"><div class="mark">“</div><p>" Lorem ipsum dolor sit amet, consectetur adipiscing elit. Maecenas sit amet velit egestas, egestas diam eu, aliquam odio ullam tempus tortor a sapien lacinia, non pellentesque elit pulvinar est qui dolorem .."</p><div class="who">- NOAH R.</div></div>
</section>

<section class="locations">
  <h2 class="heading script" style="top:56px">Our <em>Locations</em></h2>
  <div class="map" style="left:74px" role="img" aria-label="Street map of the first studio location"></div>
  <div class="loc-info" style="left:302px">
    <h4>Location Address 1</h4>
    <div class="loc-row"><svg viewBox="0 0 14 14"><path d="M7 1a4.5 4.5 0 0 0-4.5 4.5C2.5 9 7 13 7 13s4.5-4 4.5-7.5A4.5 4.5 0 0 0 7 1z" fill="#fff"/><circle cx="7" cy="5.5" r="1.6" fill="#1d1e27"/></svg><span>4120 - 4124 Harbor Lane,<br>Ashford, KT14 2PL</span></div>
    <div class="loc-row"><svg viewBox="0 0 14 14"><path d="M3 1h3l1 3-2 1.5a8 8 0 0 0 3.5 3.5L10 7l3 1v3c0 1-1 2-2 2A11 11 0 0 1 1 3c0-1 1-2 2-2z" fill="#fff"/></svg><span>+1 800 555 0142</span></div>
    <div class="loc-row"><svg viewBox="0 0 14 14"><rect x="1" y="3" width="12" height="9" rx="1" fill="#fff"/><path d="M1 4l6 4 6-4" fill="none" stroke="#1d1e27" stroke-width="1.3"/></svg><span>info@tknmusicstudios.com</span></div>
  </div>
  <div class="map" style="left:616px" role="img" aria-label="Street map of the second studio location"></div>
  <div class="loc-info" style="left:844px">
    <h4>Location Address 2</h4>
    <div class="loc-row"><svg viewBox="0 0 14 14"><path d="M7 1a4.5 4.5 0 0 0-4.5 4.5C2.5 9 7 13 7 13s4.5-4 4.5-7.5A4.5 4.5 0 0 0 7 1z" fill="#fff"/><circle cx="7" cy="5.5" r="1.6" fill="#1d1e27"/></svg><span>4120 - 4124 Harbor Lane,<br>Ashford, KT14 2PL</span></div>
    <div class="loc-row"><svg viewBox="0 0 14 14"><path d="M3 1h3l1 3-2 1.5a8 8 0 0 0 3.5 3.5L10 7l3 1v3c0 1-1 2-2 2A11 11 0 0 1 1 3c0-1 1-2 2-2z" fill="#fff"/></svg><span>+1 800 555 0142</span></div>
    <div class="loc-row"><svg viewBox="0 0 14 14"><rect x="1" y="3" width="12" height="9" rx="1" fill="#fff"/><path d="M1 4l6 4 6-4" fill="none" stroke="#1d1e27" stroke-width="1.3"/></svg><span>info@tknmusicstudios.com</span></div>
  </div>
</section>

<footer class="site-footer">
  <nav class="abs nav footer-nav">
    <span>About Us</span><span>Services</span><span>Bio's</span><span>Live Performance</span><span>Testimonials</span><span>Pre-College Prep</span><span>Affiliate Program</span><span>Shop</span><span>Contact Us</span>
  </nav>
  <p class="abs copy">Copyright © 2020 Company Name - All Right Reserved</p>
  <div class="abs footer-social"><i></i><i></i><i></i><i></i></div>
</footer>

</div>
</body>
</html>
```